uLark

We need ideas for powerpoint template. Please submit several designs from simple/basic to elaborate/detailed using our company's logo. Please match designs with our logo color. We're very open to ideas. "Harbors Harmonized" can be removed

```html
<!DOCTYPE html>
<html lang="en">
<head>
<meta charset="utf-8">
<title>uLark – Presentation Template</title>
<link rel="stylesheet" href="https://fonts.googleapis.com/css2?family=Nunito+Sans:wght@400;700;800;900&family=Roboto:wght@400&display=swap">
<style>
  :root {
    --stage: #d3d4d6;
    --teal-light: #55aeae;
    --teal-mid: #4a9aa0;
    --teal-deep: #3a7f90;
    --teal-blue: #3c7897;
    --white: #ffffff;
    --paper: #f0f2f8;
    --ink: #333333;
    --heading: "Nunito Sans", "Avenir Next", sans-serif;
    --body: "Roboto", Arial, sans-serif;
  }
  * { margin: 0; padding: 0; box-sizing: border-box; }
  html, body { width: 1200px; height: 307px; overflow: hidden; background: var(--stage); }
  .board { position: relative; width: 1200px; height: 307px; }
  .slide { position: absolute; top: 49px; width: 369px; height: 207.5px; overflow: hidden; }
  .slide--title { left: 42.5px; background: linear-gradient(90deg, var(--teal-light) 0%, var(--teal-mid) 50%, var(--teal-blue) 100%); }
  .slide--content { left: 415.5px; background: linear-gradient(180deg, var(--teal-mid) 0%, var(--teal-deep) 100%); }
  .slide--split { left: 788.5px; background: var(--paper); }
  .backdrop { position: absolute; inset: 0; width: 100%; height: 100%; }

  .slide-title { position: absolute; left: 28px; top: 94px; color: var(--white); font-family: var(--heading); letter-spacing: 0.06em; line-height: 20px; font-size: 20.5px; }
  .slide-title strong { font-weight: 900; display: block; }
  .slide-title span { font-weight: 400; display: block; }

  .brand { position: absolute; left: 231px; top: 42px; width: 102px; text-align: center; }
  .brand-disc { width: 102px; height: 102px; border-radius: 50%; background: var(--white); }
  .brand-name { margin-top: 4px; color: var(--white); font-family: var(--heading); font-weight: 700; font-size: 23px; line-height: 26px; }

  .heading { position: absolute; left: 36px; top: 79px; color: var(--white); font-family: var(--heading); font-size: 28px; line-height: 30px; }
  .heading b { font-weight: 800; }
  .heading span { font-weight: 400; }
  .copy { font-family: var(--body); font-size: 6.6px; line-height: 7.5px; text-align: justify; }
  .slide--content .copy { position: absolute; left: 36px; top: 116px; width: 306px; color: var(--white); }

  .split-heading { position: absolute; left: 34px; top: 54px; color: var(--white); font-family: var(--heading); font-size: 27px; line-height: 26px; }
  .split-heading b { font-weight: 800; display: block; }
  .split-heading span { font-weight: 400; display: block; }
  .split-sub { position: absolute; left: 34px; top: 120px; color: var(--white); font-family: var(--heading); font-size: 11.5px; }
  .slide--split .copy { position: absolute; left: 160px; top: 81px; width: 199px; color: var(--ink); }
</style>
</head>
<body>
<main class="board">

  <section class="slide slide--title">
    <svg class="backdrop" viewBox="0 0 369 207.5" aria-hidden="false">
      <defs>
        <linearGradient id="orbA" x1="0" y1="0" x2="1" y2="0">
          <stop offset="0" stop-color="#55aeae"/><stop offset="1" stop-color="#3a7f8d"/>
        </linearGradient>
        <radialGradient id="ringsA" cx="367" cy="147" r="222" gradientUnits="userSpaceOnUse">
          <stop offset="0" stop-color="#3c7897" stop-opacity="0.35"/>
          <stop offset="0.85" stop-color="#5a9fad" stop-opacity="0.25"/>
          <stop offset="1" stop-color="#5a9fad" stop-opacity="0"/>
        </radialGradient>
      </defs>
      <circle cx="18" cy="19" r="58" fill="url(#orbA)"/>
      <circle cx="367" cy="147" r="222" fill="url(#ringsA)" role="img" aria-label="Decorative concentric line texture"/>
    </svg>
    <h1 class="slide-title"><strong>PRESENTATION</strong><span>TITLE HERE</span></h1>
    <div class="brand">
      <div class="brand-disc"></div>
      <div class="brand-name">uLark</div>
    </div>
  </section>

  <section class="slide slide--content">
    <svg class="backdrop" viewBox="0 0 369 207.5">
      <defs>
        <linearGradient id="orbB" x1="0" y1="0" x2="1" y2="0">
          <stop offset="0" stop-color="#57a9aa"/><stop offset="1" stop-color="#3e8790"/>
        </linearGradient>
        <radialGradient id="ringsB" cx="369" cy="160" r="200" gradientUnits="userSpaceOnUse">
          <stop offset="0" stop-color="#5aabae" stop-opacity="0.3"/>
          <stop offset="0.9" stop-color="#5aabae" stop-opacity="0.2"/>
          <stop offset="1" stop-color="#5aabae" stop-opacity="0"/>
        </radialGradient>
      </defs>
      <circle cx="60.5" cy="20" r="26.5" fill="url(#orbB)"/>
      <circle cx="369" cy="160" r="200" fill="url(#ringsB)" role="img" aria-label="Decorative concentric line texture"/>
    </svg>
    <h2 class="heading"><b>Lorem</b> <span>Ipsum</span></h2>
    <p class="copy">Lorem ipsum dolor sit amet, consectetur adipiscing elit. Ut at vehicula dui, quis vulputate ipsum. Nunc et bibendum nunc. Fusce suscipit feugiat fringilla. Aliquam quis tincidunt orci, quis gravida ex. Cras suscipit placerat lorem, in dictum enim aliquam eget. Aenean porttitor arcu ex, quis mattis sapien ullamcorper eget. Proin imperdiet vel nisi a volutpat. Fusce elit purus, tincidunt et viverra ut, maximus sit amet turpis.</p>
  </section>

  <section class="slide slide--split">
    <svg class="backdrop" viewBox="0 0 369 207.5">
      <defs>
        <linearGradient id="panel" x1="0" y1="0" x2="0" y2="1">
          <stop offset="0" stop-color="#55aeae"/><stop offset="1" stop-color="#3a808f"/>
        </linearGradient>
      </defs>
      <path d="M0 0H111C136 30 147 65 147 100C147 140 130 176 102 207.5H0Z" fill="url(#panel)"/>
    </svg>
    <h2 class="split-heading"><b>Lorem</b><span>Ipsum</span></h2>
    <p class="split-sub">dolor sit amet</p>
    <p class="copy">Lorem ipsum dolor sit amet, consectetur adipiscing elit. Ut at vehicula dui, quis vulputate ipsum. Nunc et bibendum nunc. Fusce suscipit feugiat fringilla. Aliquam quis tincidunt orci, quis gravida ex. Cras suscipit placerat lorem, in dictum enim aliquam eget. Aenean porttitor arcu ex, quis mattis sapien ullamcorper eget. Proin imperdiet vel nisi a volutpat. Fusce elit purus, tincidunt et viverra ut, maximus sit amet turpis.</p>
  </section>

</main>
</body>
</html>
```